LED panel tester - hand-held test tool - simple label required

I have designed a product to test the LED panels of a road-side variable message sign (VMS). I don't expect to sell too many of these but thought it would look professional if it had a proper label.

I need a label designed for this hand-held test equipment. Attached is the positional layout of all the switches and text. I have also included a photo of the product.

A simple Google image search of "hand-held test tool" shows that it doesn't have to be fancy but rather functional.

I would like to put branding on the bottom 1/5th and have the option to interchange the brand if I ever get approached by one of the manufacturers of these signs. Initially it will just have a link to my website (BrightKettleWorks.com.au) right down at the bottom.

```html
<!DOCTYPE html>
<html lang="en">
<head>
<meta charset="utf-8">
<title>VMS Panel Tester – Label Variants</title>
<link href="https://fonts.googleapis.com/css2?family=Fira+Sans+Condensed:wght@500;600;800&display=swap" rel="stylesheet">
<style>
  :root {
    --page: #ffffff;
    --body: #000000;
    --ink: #ffffff;
    --brand-blue: #0061ba;
    --brand-grey: #4a4a4a;
  }
  html, body {
    margin: 0;
    padding: 0;
    width: 1200px;
    height: 1200px;
    overflow: hidden;
    background: var(--page);
  }
  .sheet {
    position: relative;
    width: 1200px;
    height: 1200px;
    font-family: "Fira Sans Condensed", "Arial Narrow", sans-serif;
  }
  .label {
    position: absolute;
    top: 71px;
    width: 462px;
    height: 1065px;
    background: var(--body);
    overflow: hidden;
  }
  .label--blue { left: 119px; --accent: var(--brand-blue); }
  .label--grey { left: 626px; --accent: var(--brand-grey); }

  .label__art {
    position: absolute;
    inset: 0;
    width: 462px;
    height: 1065px;
  }
  .label__header,
  .label__footer {
    position: absolute;
    left: 0;
    width: 100%;
    background: var(--accent);
    color: var(--ink);
    display: flex;
    align-items: center;
    justify-content: center;
    white-space: nowrap;
  }
  .label__header {
    top: 0;
    height: 68px;
    font-weight: 800;
    font-size: 35px;
    letter-spacing: 0.3px;
  }
  .label__footer {
    bottom: 0;
    height: 56px;
    font-weight: 500;
    font-size: 27px;
    letter-spacing: 0.2px;
  }

  .pattern-field { fill: url(#field-fade); }
  .outline {
    fill: var(--body);
    stroke: var(--accent);
    stroke-width: 4;
  }
  .display-window {
    fill: none;
    stroke: var(--accent);
    stroke-width: 1.5;
  }
  .key-text {
    fill: var(--ink);
    font-family: "Fira Sans Condensed", "Arial Narrow", sans-serif;
    font-weight: 600;
    font-size: 21px;
    dominant-baseline: central;
  }
</style>
</head>
<body>
<div class="sheet">

  <!-- Blue variant -->
  <section class="label label--blue">
    <svg class="label__art" viewBox="0 0 462 1065" xmlns="http://www.w3.org/2000/svg">
      <defs>
        <radialGradient id="field-fade" cx="50%" cy="70%" r="75%">
          <stop offset="0" stop-color="#06152a"/>
          <stop offset="1" stop-color="#000000"/>
        </radialGradient>
      </defs>
      <rect class="pattern-field" x="0" y="68" width="462" height="941" role="img" aria-label="Circuit-board trace pattern in blue lines on black"/>

      <g class="buttons">
        <circle class="outline" cx="231" cy="199" r="31"/>
        <circle class="outline" cx="231" cy="269" r="31"/>
        <circle class="outline" cx="231" cy="340" r="31"/>
        <circle class="outline" cx="231" cy="410" r="31"/>
        <circle class="outline" cx="231" cy="481" r="31"/>
        <circle class="outline" cx="231" cy="552" r="31"/>
        <circle class="outline" cx="386" cy="659" r="22"/>
      </g>

      <g class="keys">
        <rect class="outline" x="282" y="181" width="74" height="36" rx="18"/>
        <text class="key-text" x="299" y="199">RED</text>
        <rect class="outline" x="282" y="251" width="107" height="36" rx="18"/>
        <text class="key-text" x="299" y="269">GREEN</text>
        <rect class="outline" x="282" y="322" width="124" height="36" rx="18"/>
        <text class="key-text" x="299" y="340">ORANGE</text>
        <rect class="outline" x="282" y="392" width="102" height="36" rx="18"/>
        <text class="key-text" x="300" y="410">WHITE</text>
        <rect class="outline" x="282" y="463" width="84" height="36" rx="18"/>
        <text class="key-text" x="299" y="481">BLUE</text>
        <rect class="outline" x="282" y="534" width="93" height="36" rx="18"/>
        <text class="key-text" x="300" y="552">SLOW</text>
        <rect class="outline" x="92" y="534" width="87" height="36" rx="18"/>
        <text class="key-text" x="110" y="552">FAST</text>
        <rect class="outline" x="342" y="693" width="89" height="36" rx="18"/>
        <text class="key-text" x="349" y="711">POWER</text>
      </g>

      <rect class="outline" x="129" y="639" width="203" height="145" rx="5"/>
      <rect class="display-window" x="141" y="653" width="180" height="118"/>
    </svg>
    <header class="label__header">VMS PANEL TESTER</header>
    <footer class="label__footer">www.BrightKettleWorks.com.au</footer>
  </section>

  <!-- Grey variant -->
  <section class="label label--grey">
    <svg class="label__art" viewBox="0 0 462 1065" xmlns="http://www.w3.org/2000/svg">
      <defs>
        <radialGradient id="field-fade-grey" cx="50%" cy="70%" r="75%">
          <stop offset="0" stop-color="#141414"/>
          <stop offset="1" stop-color="#000000"/>
        </radialGradient>
      </defs>
      <rect x="0" y="68" width="462" height="941" fill="url(#field-fade-grey)" role="img" aria-label="Circuit-board trace pattern in grey lines on black"/>

      <g class="buttons">
        <circle class="outline" cx="231" cy="199" r="31"/>
        <circle class="outline" cx="231" cy="269" r="31"/>
        <circle class="outline" cx="231" cy="340" r="31"/>
        <circle class="outline" cx="231" cy="410" r="31"/>
        <circle class="outline" cx="231" cy="481" r="31"/>
        <circle class="outline" cx="231" cy="552" r="31"/>
        <circle class="outline" cx="386" cy="659" r="22"/>
      </g>

      <g class="keys">
        <rect class="outline" x="282" y="181" width="74" height="36" rx="18"/>
        <text class="key-text" x="299" y="199">RED</text>
        <rect class="outline" x="282" y="251" width="107" height="36" rx="18"/>
        <text class="key-text" x="299" y="269">GREEN</text>
        <rect class="outline" x="282" y="322" width="124" height="36" rx="18"/>
        <text class="key-text" x="299" y="340">ORANGE</text>
        <rect class="outline" x="282" y="392" width="102" height="36" rx="18"/>
        <text class="key-text" x="300" y="410">WHITE</text>
        <rect class="outline" x="282" y="463" width="84" height="36" rx="18"/>
        <text class="key-text" x="299" y="481">BLUE</text>
        <rect class="outline" x="282" y="534" width="93" height="36" rx="18"/>
        <text class="key-text" x="300" y="552">SLOW</text>
        <rect class="outline" x="92" y="534" width="87" height="36" rx="18"/>
        <text class="key-text" x="110" y="552">FAST</text>
        <rect class="outline" x="342" y="693" width="89" height="36" rx="18"/>
        <text class="key-text" x="349" y="711">POWER</text>
      </g>

      <rect class="outline" x="129" y="639" width="203" height="145" rx="5"/>
      <rect class="display-window" x="141" y="653" width="180" height="118"/>
    </svg>
    <header class="label__header">VMS PANEL TESTER</header>
    <footer class="label__footer">www.BrightKettleWorks.com.au</footer>
  </section>

</div>
</body>
</html>
```